Brightmoor Towing Website

New Pittsburgh, PA towing company looking for a unique and easy to use website with a professional look. We would like the customer to feel confident when booking with us. We offer reliable services with no hidden fees or predatory towing tactics. Designs that incorporate our logo & color scheme are preferred. Looking for websites designed similar to https://calverlyhaulservice.com/

```html
<!DOCTYPE html>
<html lang="en">
<head>
<meta charset="utf-8">
<title>Brightmoor Towing</title>
<link rel="stylesheet" href="https://fonts.googleapis.com/css2?family=Raleway:wght@400;500;600;700;800&display=swap">
<style>
:root{
  --maroon:#6a1212;
  --maroon-deep:#4e0c0c;
  --ink:#151515;
  --dark:#1a1a1a;
  --gold:#d2a532;
  --gold-soft:#e4bb47;
  --text:#222;
  --muted:#555;
  --line:#dedede;
  --white:#fff;
}
*{box-sizing:border-box;margin:0;padding:0}
html,body{width:1200px;height:5106px;overflow:hidden}
body{font-family:"Raleway",Arial,sans-serif;color:var(--text);background:var(--white);position:relative}
section,header,footer{position:absolute;left:0;width:1200px}
.abs{position:absolute}
.btn{position:absolute;display:flex;align-items:center;justify-content:center;border-radius:24px;font-weight:700;font-size:15px;text-transform:uppercase;letter-spacing:.2px}
.btn-maroon{background:var(--maroon);color:var(--white)}
.btn-gold{background:var(--gold);color:var(--ink)}
.heading{font-weight:800;text-transform:uppercase;letter-spacing:.3px}
.photo{position:absolute}

/* header */
.site-header{top:0;height:100px;background:var(--ink)}
.brand{left:120px;top:38px;font-weight:700;font-size:26px;color:var(--gold)}
.nav{left:374px;top:70px}
.nav a{color:var(--white);text-decoration:none;font-size:16px;font-weight:500;position:absolute;white-space:nowrap}
.nav a.active{color:var(--gold)}
.hotline{left:714px;top:12px;display:flex;align-items:center;gap:8px}
.hotline-badge{width:36px;height:36px;border-radius:50%;background:var(--gold);color:var(--ink);font-weight:800;font-size:13px;display:flex;align-items:center;justify-content:center}
.hotline small{display:block;color:var(--white);font-size:10px;font-weight:600}
.hotline strong{display:block;color:var(--gold);font-size:17px;font-weight:600;white-space:nowrap}
.social{display:flex;gap:6px}
.social span{width:36px;height:36px;border-radius:50%;background:var(--gold);display:block}

/* hero */
.hero{top:100px;height:624px}
.hero-shade{left:0;top:0;width:1200px;height:624px;background:linear-gradient(90deg,rgba(0,0,0,.55),rgba(0,0,0,.1) 60%,rgba(0,0,0,0))}
.hero h1{left:105px;top:200px;font-size:66px;font-weight:800;color:var(--white);letter-spacing:.5px}
.hero p{left:115px;top:280px;width:480px;font-size:18px;line-height:27px;color:var(--white);font-weight:500}
.arrow{position:absolute}
.dots{left:558px;top:582px;display:flex;gap:12px}
.dots i{width:12px;height:12px;border-radius:50%;background:rgba(255,255,255,.45);display:block}
.dots i:first-child{background:var(--white)}

/* features */
.features{top:724px;height:387px;background:var(--maroon)}
.feature{position:absolute;top:58px;width:320px;text-align:center;color:var(--white)}
.feature .icon{width:104px;height:104px;border:2px solid rgba(255,255,255,.85);border-radius:50%;margin:0 auto;display:flex;align-items:center;justify-content:center}
.feature h3{margin-top:38px;font-size:15px;font-weight:700;text-transform:uppercase}
.feature p{margin-top:12px;font-size:13px;line-height:26px;padding:0 8px}

/* about */
.about{top:1111px;height:591px}
.about-photo{left:125px;top:91px;width:442px;height:409px;border-radius:10px;background:linear-gradient(180deg,#6d95c6 0%,#9fbbd8 45%,#6a2a2a 60%,#7a7570 80%,#8c8a80 100%)}
.about h2{left:655px;top:140px;font-size:34px}
.about p{left:655px;top:196px;width:430px;font-size:13px;line-height:26px;color:var(--muted)}

/* call band */
.call-band{top:1702px;height:203px}
.call-icon{left:554px;top:-38px;width:92px;height:92px;border-radius:50%;background:var(--gold);display:flex;align-items:center;justify-content:center}
.call-band .num{left:0;width:1200px;top:80px;text-align:center;color:var(--white);font-size:27px;font-weight:700}
.call-band .sub{left:0;width:1200px;top:118px;text-align:center;color:var(--white);font-size:22px;font-weight:500}

/* services */
.services{top:1905px;height:738px}
.center-title{left:0;width:1200px;text-align:center;font-size:32px}
.intro{left:230px;width:740px;text-align:center;font-size:17px;line-height:26px;color:var(--muted)}
.service-card{position:absolute;top:224px;width:314px;height:430px;border:1px solid var(--line);border-radius:4px;text-align:center;background:var(--white)}
.service-card .photo{left:0;top:0;width:312px;height:217px;border-radius:4px 4px 0 0}
.service-card h3{position:absolute;top:236px;left:0;width:100%;font-size:20px;font-weight:700;text-transform:uppercase}
.service-card p{position:absolute;top:274px;left:22px;width:270px;font-size:12.5px;line-height:25px;color:var(--muted)}
.service-card .btn{left:77px;top:364px;width:160px;height:44px;font-size:14px}

/* testimonials */
.testimonials{top:2643px;height:571px}
.testimonials .center-title,.testimonials .intro{color:var(--white)}
.quote-card{position:absolute;top:208px;width:316px;height:157px;background:var(--white);padding:22px 18px;font-size:15px;line-height:26px;color:var(--text)}
.reviewer{position:absolute;top:384px;display:flex;align-items:center;gap:14px}
.avatar{position:relative;width:88px;height:88px;border-radius:50%;background:radial-gradient(circle,#c9b7a8,#8b7262)}
.avatar b{position:absolute;left:-4px;bottom:-2px;width:34px;height:34px;border-radius:50%;background:var(--gold);color:var(--white);font-size:24px;font-weight:800;display:flex;align-items:center;justify-content:center;line-height:1;padding-top:10px}
.reviewer h4{color:var(--white);font-size:18px;font-weight:800;text-transform:uppercase}
.stars{color:var(--gold-soft);font-size:16px;letter-spacing:1px}

/* gallery */
.gallery{top:3214px;height:734px}
.gallery .photo{width:316px;height:270px}

/* partners */
.partners{top:3948px;height:238px}
.partner{position:absolute;top:128px;display:flex;align-items:center;gap:8px;font-size:20px;font-weight:700;color:#222;white-space:nowrap}
.partner i{display:block;width:20px;height:20px;background:#222}
.partner i.round{border-radius:50%}

/* contact */
.contact-bg{top:4628px;height:478px;background:var(--ink)}
.contact-card{left:131px;top:4230px;width:944px;height:512px;border-radius:8px;overflow:hidden;background:var(--white);box-shadow:0 6px 20px rgba(0,0,0,.15)}
.contact-info{position:absolute;left:0;top:0;width:438px;height:512px;background:var(--dark);color:var(--white)}
.contact-info .logo{position:absolute;left:44px;top:140px;font-weight:700;font-size:44px;color:var(--gold)}
.info-row{position:absolute;left:44px;display:flex;gap:8px;font-size:17px;align-items:flex-start}
.info-row.sm{font-size:14px}
.follow{position:absolute;left:36px;top:398px;font-size:17px;font-weight:700}
.ring-social{position:absolute;left:44px;top:432px;display:flex;gap:6px}
.ring-social span{width:28px;height:28px;border-radius:50%;border:1.5px solid var(--white);display:block}
.contact-form{position:absolute;left:480px;top:0}
.contact-form h2{position:absolute;left:0;top:46px;font-size:36px;white-space:nowrap}
.contact-form .lead{position:absolute;left:0;top:100px;font-size:15px;font-weight:700;white-space:nowrap}
.field{position:absolute;left:0;width:381px;height:44px;border:1px solid var(--line);display:flex;align-items:center;padding-left:14px;font-size:13px;color:#999;gap:7px}
.field.msg{height:103px;align-items:flex-start;padding-top:14px}
.contact-form .btn{left:113px;top:430px;width:155px;height:44px;font-size:15px}

/* footer */
.site-footer{top:4742px;height:364px;color:var(--white)}
.fcol{position:absolute;top:64px}
.fcol h4{font-size:19px;font-weight:600;margin-bottom:10px}
.fcol li{list-style:none;font-size:14px;line-height:28px}
.fcol p{font-size:14px;line-height:28px;width:310px}
.rule{left:111px;top:299px;width:978px;height:1px;background:#444}
.copy{left:0;width:1200px;top:320px;text-align:center;font-size:14px}
</style>
</head>
<body>

<header class="site-header">
  <div class="abs brand">Brightmoor</div>
  <nav class="abs nav">
    <a class="active" style="left:0">HOME</a>
    <a style="left:114px">SERVICES</a>
    <a style="left:255px">REVIEWS</a>
    <a style="left:392px">ABOUT</a>
    <a style="left:517px">AREAS</a>
    <a style="left:635px">CONTACT</a>
  </nav>
  <div class="abs hotline">
    <div class="hotline-badge">24</div>
    <div><small>24 HOURS TOWING</small><strong>412 - 555 - 0187</strong></div>
  </div>
  <div class="abs social" style="left:924px;top:14px">
    <span></span><span></span><span></span><span></span>
  </div>
</header>

<section class="hero">
  <div class="photo" role="img" aria-label="Red flatbed tow truck carrying a red car" style="left:0;top:0;width:1200px;height:624px;background:linear-gradient(90deg,#2a2120 0%,#4a3532 40%,#9a2424 68%,#5c4a46 100%)"></div>
  <div class="abs hero-shade"></div>
  <h1 class="abs">BRIGHTMOOR</h1>
  <p class="abs">The team at Brightmoor Towing is licensed and equipped to complete local and long-distance equipment transportation projects. Call</p>
  <div class="btn btn-maroon" style="left:111px;top:392px;width:171px;height:44px">Call Us Now</div>
  <div class="btn btn-gold" style="left:298px;top:392px;width:220px;height:44px">Schedule Service</div>
  <svg class="arrow" style="left:62px;top:298px" width="20" height="32" viewBox="0 0 20 32"><path d="M16 2 4 16l12 14" fill="none" stroke="#fff" stroke-width="2"/></svg>
  <svg class="arrow" style="left:1116px;top:298px" width="20" height="32" viewBox="0 0 20 32"><path d="M4 2l12 14L4 30" fill="none" stroke="#fff" stroke-width="2"/></svg>
  <div class="abs dots"><i></i><i></i><i></i><i></i></div>
</section>

<section class="features">
  <div class="feature" style="left:100px">
    <div class="icon"><svg width="56" height="56" viewBox="0 0 56 56" fill="none" stroke="#fff" stroke-width="2"><circle cx="19" cy="18" r="7"/><circle cx="37" cy="18" r="7"/><circle cx="28" cy="34" r="5"/><path d="M6 48c0-9 6-14 13-14M50 48c0-9-6-14-13-14M18 50c0-6 4-9 10-9s10 3 10 9"/></svg></div>
    <h3>Family Owned &amp; Operated</h3>
    <p>Lorem ipsum dolor sit amet, cctetur adipiscing elit, sed do eiusmod tempor incidunt ut labore et dolore magna aua. Quis ipsum suspendisse ultrices gravida. Risus commodo</p>
  </div>
  <div class="feature" style="left:441px">
    <div class="icon"><svg width="60" height="50" viewBox="0 0 60 50" fill="none" stroke="#fff" stroke-width="2"><path d="M4 36h52M8 36V24l6-8h12v20M26 24h26v12M40 24l10-14M50 10l4 4"/><circle cx="16" cy="40" r="4"/><circle cx="44" cy="40" r="4"/></svg></div>
    <h3>Roadside Assistance</h3>
    <p>Lorem ipsum dolor sit amet, cctetur adipiscing elit, sed do eiusmod tempor incidunt ut labore et dolore magna aua. Quis ipsum suspendisse ultrices gravida. Risus commodo</p>
  </div>
  <div class="feature" style="left:780px">
    <div class="icon"><svg width="60" height="60" viewBox="0 0 60 60" fill="none" stroke="#fff" stroke-width="2"><path d="M50 22A22 22 0 1 0 52 34"/><path d="M52 14v9h-9"/><text x="30" y="36" text-anchor="middle" fill="#fff" stroke="none" font-family="Raleway,sans-serif" font-weight="800" font-size="15">24/7</text></svg></div>
    <h3>24 Hour Emergency Service</h3>
    <p>Lorem ipsum dolor sit amet, cctetur adipiscing elit, sed do eiusmod tempor incidunt ut labore et dolore magna aua. Quis ipsum suspendisse ultrices gravida. Risus commodo</p>
  </div>
</section>

<section class="about">
  <div class="photo about-photo" role="img" aria-label="Heavy-duty red tow truck under a blue sky"></div>
  <h2 class="abs heading">About Us</h2>
  <p class="abs">Lorem ipsum dolor sit amet, consectetur adipiscing elit, sed do eiusmod tempor incididunt ut labore et dolore magna aliqua.is ipsum suspendisse ultrices gravida. Risus commodo viverra maecenas accumsan lacus vel facilisis. Lorem ipsum dolor sit amet, consectetur adipiscing elit, sed do eiusmod tempor incididunt ut labore et dolore magna aliqua. Quis ipsum suspendisse ultrices gravida. Risus commodo viverra maecenas accumsan lacus vel facilisis.</p>
  <div class="btn btn-maroon" style="left:661px;top:396px;width:175px;height:46px">Learn More</div>
</section>

<section class="call-band">
  <div class="photo" role="img" aria-label="Driver on the phone beside a broken-down car" style="left:0;top:0;width:1200px;height:203px;background:linear-gradient(90deg,#4e0c0c,#6d1a18 60%,#7a2a22)"></div>
  <div class="abs call-icon"><svg width="40" height="40" viewBox="0 0 24 24" fill="#fff"><path d="M6.6 10.8a15.1 15.1 0 0 0 6.6 6.6l2.2-2.2c.3-.3.7-.4 1-.2 1.1.4 2.3.6 3.6.6.6 0 1 .4 1 1V20c0 .6-.4 1-1 1A17 17 0 0 1 3 4c0-.6.4-1 1-1h3.5c.6 0 1 .4 1 1 0 1.3.2 2.5.6 3.6.1.3 0 .7-.2 1z"/></svg></div>
  <div class="abs num">(412) - 555 - 0187</div>
  <div class="abs sub">NEED MORE INFORMATION GET IMMEDIATE HELP 24/7</div>
</section>

<section class="services">
  <h2 class="abs heading center-title" style="top:80px">Our Services</h2>
  <p class="abs intro" style="top:130px">Lorem ipsum dolor sit amet, consectetur adipiscing elit, sed do eiusmod tempor incididunt ut labore et dolore magna aliqua. Quis ipsum suspendisse ultrices gravida.</p>
  <div class="service-card" style="left:111px">
    <div class="photo" role="img" aria-label="Yellow flatbed truck loading a car" style="background:linear-gradient(180deg,#b9c9d6 0%,#d9b640 45%,#6d6d70 75%,#8c8c8c 100%)"></div>
    <h3>Towing Soultions</h3>
    <p>Lorem ipsum dolor sit amet, consectetur adipiscing elit, sed do eiusmod tempor incididunt ut labore et dolore magna aliqua.</p>
    <div class="btn btn-maroon">Learn More</div>
  </div>
  <div class="service-card" style="left:444px">
    <div class="photo" role="img" aria-label="Tow operator in a truck cab" style="background:linear-gradient(180deg,#e9e9e9 0%,#c7b8a8 40%,#a8432e 70%,#d6d6d6 100%)"></div>
    <h3>Roadside Assistance</h3>
    <p>Lorem ipsum dolor sit amet, consectetur adipiscing elit, sed do eiusmod tempor incididunt ut labore et dolore magna aliqua.</p>
    <div class="btn btn-maroon">Learn More</div>
  </div>
  <div class="service-card" style="left:776px">
    <div class="photo" role="img" aria-label="Tow truck with a red car on a tree-lined road" style="background:linear-gradient(180deg,#a9c4de 0%,#3f6b3a 40%,#557a45 70%,#8d8f86 100%)"></div>
    <h3>Emergency Towing</h3>
    <p>Lorem ipsum dolor sit amet, consectetur adipiscing elit, sed do eiusmod tempor incididunt ut labore et dolore magna aliqua.</p>
    <div class="btn btn-maroon">Learn More</div>
  </div>
</section>

<section class="testimonials">
  <div class="photo" role="img" aria-label="Tow truck at night in deep red tones" style="left:0;top:0;width:1200px;height:571px;background:linear-gradient(90deg,#4e0c0c,#6b1616 50%,#5a1212)"></div>
  <h2 class="abs heading center-title" style="top:78px">Testimonials</h2>
  <p class="abs intro" style="top:126px">Lorem ipsum dolor sit amet, consectetur adipiscing elit, sed do eiusmod tempor incididunt ut labore et dolore magna aliqua. Quis ipsum suspendisse ultrices gravida.</p>
  <svg class="arrow" style="left:84px;top:270px" width="16" height="30" viewBox="0 0 16 30"><path d="M14 2 3 15l11 13" fill="none" stroke="#fff" stroke-width="2"/></svg>
  <svg class="arrow" style="left:1098px;top:270px" width="16" height="30" viewBox="0 0 16 30"><path d="M2 2l11 13L2 28" fill="none" stroke="#fff" stroke-width="2"/></svg>

  <div class="quote-card" style="left:111px">Lorem ipsum dolor sit amet, consectetur adipiscing elit, sed do eiusmod tempor incididunt ut labore et dolore magna aliqua. Quis ipsum suspendisse</div>
  <div class="quote-card" style="left:442px">Lorem ipsum dolor sit amet, consectetur adipiscing elit, sed do eiusmod tempor incididunt ut labore et dolore magna aliqua. Quis ipsum suspendisse</div>
  <div class="quote-card" style="left:773px">Lorem ipsum dolor sit amet, consectetur adipiscing elit, sed do eiusmod tempor incididunt ut labore et dolore magna aliqua. Quis ipsum suspendisse</div>

  <div class="reviewer" style="left:111px"><div class="avatar" role="img" aria-label="Customer portrait"><b>“</b></div><div><h4>Daniel Reyes</h4><div class="stars">★★★★★</div></div></div>
  <div class="reviewer" style="left:442px"><div class="avatar" role="img" aria-label="Customer portrait"><b>“</b></div><div><h4>Daniel Reyes</h4><div class="stars">★★★★★</div></div></div>
  <div class="reviewer" style="left:773px"><div class="avatar" role="img" aria-label="Customer portrait"><b>“</b></div><div><h4>Daniel Reyes</h4><div class="stars">★★★★★</div></div></div>
</section>

<section class="gallery">
  <h2 class="abs heading center-title" style="top:78px">Our Gallery</h2>
  <div class="photo" role="img" aria-label="Flatbed truck carrying a red sports car" style="left:111px;top:133px;background:linear-gradient(180deg,#5f6a4a,#8a8f7d 45%,#c22a2a 65%,#555 100%)"></div>
  <div class="photo" role="img" aria-label="Red tow truck wheel lift in the woods" style="left:442px;top:133px;background:linear-gradient(180deg,#405a30,#b9302c 45%,#3a3a3a 80%,#6a6a6a)"></div>
  <div class="photo" role="img" aria-label="Grey car loaded on a flatbed" style="left:774px;top:133px;background:linear-gradient(180deg,#9eb4c9,#7a7d82 45%,#c4413a 70%,#9a9a9a)"></div>
  <div class="photo" role="img" aria-label="Black SUV on a tow truck bed" style="left:111px;top:419px;background:linear-gradient(180deg,#c8d3dd,#4a4f56 45%,#2a2a2a 75%,#8c8c8c)"></div>
  <div class="photo" role="img" aria-label="White car being winched onto a flatbed" style="left:442px;top:419px;background:linear-gradient(180deg,#dfe3e6,#b6b9bc 45%,#5a5a5a 75%,#a5a5a5)"></div>
  <div class="photo" role="img" aria-label="Tow truck under a cloudy sky" style="left:774px;top:419px;background:linear-gradient(180deg,#a6b3bd,#6f7a80 45%,#7d2a28 65%,#4f5458)"></div>
</section>

<section class="partners">
  <h2 class="abs heading center-title" style="top:66px">Partners and Sponsors</h2>
  <div class="partner" style="left:113px"><i></i>Northfield Co</div>
  <div class="partner" style="left:310px"><i class="round"></i>Relaymail</div>
  <div class="partner" style="left:498px"><i></i>Lumenworks</div>
  <div class="partner" style="left:690px"><i class="round"></i>Kestrel</div>
  <div class="partner" style="left:930px"><i></i>ORBITLINE</div>
</section>

<section class="contact-bg"></section>
<div class="abs contact-card">
  <div class="contact-info">
    <div class="logo">Brightmoor</div>
    <div class="info-row" style="top:256px"><svg width="14" height="18" viewBox="0 0 14 18" style="margin-top:3px"><path d="M7 1a6 6 0 0 0-6 6c0 4.5 6 10 6 10s6-5.5 6-10a6 6 0 0 0-6-6z" fill="none" stroke="#fff" stroke-width="1.6"/><circle cx="7" cy="7" r="2" fill="#fff"/></svg><span>4410 Larkfield Avenue Pittsburgh<br>PA 15212</span></div>
    <div class="info-row sm" style="top:326px"><svg width="14" height="14" viewBox="0 0 24 24" fill="#fff"><path d="M6.6 10.8a15.1 15.1 0 0 0 6.6 6.6l2.2-2.2c.3-.3.7-.4 1-.2 1.1.4 2.3.6 3.6.6.6 0 1 .4 1 1V20c0 .6-.4 1-1 1A17 17 0 0 1 3 4c0-.6.4-1 1-1h3.5c.6 0 1 .4 1 1 0 1.3.2 2.5.6 3.6.1.3 0 .7-.2 1z"/></svg><span>412 - 555 - 0187</span></div>
    <div class="info-row sm" style="top:362px"><svg width="16" height="12" viewBox="0 0 16 12"><rect x="1" y="1" width="14" height="10" fill="none" stroke="#fff" stroke-width="1.5"/><path d="M1 1l7 6 7-6" fill="none" stroke="#fff" stroke-width="1.5"/></svg><span>info@Brightmoor.com</span></div>
    <div class="follow">Follow Us On</div>
    <div class="ring-social"><span></span><span></span><span></span></div>
  </div>
  <div class="contact-form">
    <h2 class="heading">Contact Us</h2>
    <div class="lead">Please describe your project or specific needs</div>
    <div class="field" style="top:147px">👤 Name</div>
    <div class="field" style="top:202px">✉ Email Address</div>
    <div class="field" style="top:258px">☎ Contact No</div>
    <div class="field msg" style="top:313px">✎ Message</div>
    <div class="btn btn-maroon">Submit</div>
  </div>
</div>

<footer class="site-footer">
  <div class="fcol" style="left:111px"><h4>Our Services</h4><ul><li>Light-Duty Towing</li><li>Accident Recovery</li><li>Roadside Assistance</li><li>Lockout Service</li><li>Battery Service</li><li>More</li></ul></div>
  <div class="fcol" style="left:349px"><h4>Qucik Links</h4><ul><li>Home</li><li>Services</li><li>Reviews</li><li>About</li><li>Areas</li><li>Contact</li></ul></div>
  <div class="fcol" style="left:569px"><h4>Resources</h4><ul><li>Support</li><li>Testimonials</li><li>Sitemap</li><li>Career</li><li>Contact Us</li></ul></div>
  <div class="fcol" style="left:778px"><h4>About</h4><p>Lorem ipsum dolor sit amet, consectetur adipiscing elit, sed do eiusmod tempor incididunt ut labore et dolore magna aliqua. Quis ipsum suspendisse ultrices gravida. Risus</p></div>
  <div class="abs rule"></div>
  <div class="abs copy">Copyright © Brightmoor. All rights reserved.</div>
</footer>

</body>
</html>
```